Lanternfield Advisory logo/business card design -- a digital consulting company

I've just restarted a consulting company I had years ago--Lanternfield Advisory. Now I need a new business card and updated logo. The original logo was simple enough: a chart-like progression atop a grid (see the attached file). I do strategy work, and the chart is meant to show incremental growth and profit. I'd like the reincarnation of my logo to be 3D, with both the grid and arrow rotated on their axis.

I'll want to use the logo on my website as well. I'm open to color schemes, fonts, etc.

Target Market(s)

Business-to-Business. Target market is corporate.

Industry/Entity Type

Business

Contact Information for Business Card

Logo on one-side; name and other contact info on the back

Font styles to use
Serif
Sans Serif

Requirements
Nice to have
• Lanternfield Advisory refers to the concept of "bootstrapping" or making incremental changes to grow with minimal risk and financial exposure, and self-sufficiency (think of the phrase "to pull oneself by one's bootstraps.")

```html
<!DOCTYPE html>
<html lang="en">
<head>
<meta charset="utf-8">
<title>Lanternfield Advisory – Logo and Business Card</title>
<link href="https://fonts.googleapis.com/css2?family=Montserrat:wght@400;600;700&display=swap" rel="stylesheet">
<style>
  :root {
    --bg: #ffffff;
    --green: #4cb848;
    --green-dark: #2e8b3a;
    --green-light: #8cc63f;
    --ink: #222222;
    --grey: #6d6d6d;
    --card-white: #ffffff;
    --card-black: #050505;
    --edge: #d9d9d9;
  }
  * { margin: 0; padding: 0; box-sizing: border-box; }
  html, body { width: 1200px; height: 1000px; overflow: hidden; }
  body {
    background: var(--bg);
    font-family: "Montserrat", Arial, sans-serif;
    position: relative;
  }

  /* Standalone logo */
  .brand-logo {
    position: absolute;
    left: 760px;
    top: 270px;
    width: 380px;
    display: flex;
    align-items: center;
    gap: 14px;
  }
  .brand-square {
    width: 34px; height: 34px;
    background: var(--green);
    flex: none;
  }
  .brand-name {
    color: var(--green);
    font-weight: 700;
    font-size: 30px;
    line-height: 1.05;
    letter-spacing: 1px;
    text-transform: uppercase;
  }

  /* Cards */
  .card {
    position: absolute;
    width: 560px;
    height: 320px;
    border-radius: 4px;
    overflow: hidden;
  }
  .card-back {
    left: 60px; top: 300px;
    background: var(--card-white);
    border: 1px solid var(--edge);
    box-shadow: 0 2px 0 var(--edge), 0 4px 0 var(--edge);
  }
  .card-front {
    left: 590px; top: 590px;
    background: var(--card-black);
    display: flex;
    align-items: center;
    justify-content: center;
  }

  .name-band {
    position: absolute;
    left: 0; top: 60px;
    width: 270px;
    height: 66px;
    background: var(--green);
    clip-path: polygon(0 0, 100% 0, 88% 100%, 0 100%);
    padding: 10px 0 0 26px;
    color: #fff;
  }
  .name-band::after {
    content: "";
    position: absolute;
    right: 0; top: 0;
    width: 22px; height: 66px;
    background: var(--green-dark);
  }
  .person-name { font-weight: 700; font-size: 24px; line-height: 1.1; }
  .person-role { font-weight: 400; font-size: 15px; }

  .cities {
    position: absolute;
    left: 26px; top: 162px;
    font-size: 13px;
    color: var(--ink);
    letter-spacing: 0.5px;
  }
  .contact-list {
    position: absolute;
    left: 26px; top: 196px;
    list-style: none;
    font-size: 13px;
    color: var(--ink);
  }
  .contact-list li {
    display: flex;
    align-items: center;
    gap: 10px;
    height: 30px;
  }
  .contact-icon { width: 20px; height: 20px; flex: none; }

  .card-front .brand-square { width: 40px; height: 40px; }
  .card-front .brand-name { font-size: 34px; }
  .front-logo { display: flex; align-items: center; gap: 16px; }
</style>
</head>
<body>

  <div class="brand-logo">
    <span class="brand-square"></span>
    <span class="brand-name">Lanternfield Advisory</span>
  </div>

  <section class="card card-back" aria-label="Business card, contact side">
    <div class="name-band">
      <div class="person-name">Morgan Hale</div>
      <div class="person-role">Graphic Artist</div>
    </div>
    <p class="cities">NEW YORK | LAS VEGAS | SYDNEY</p>
    <ul class="contact-list">
      <li>
        <svg class="contact-icon" viewBox="0 0 20 20" aria-hidden="true">
          <polygon points="10,1 18,5.5 18,14.5 10,19 2,14.5 2,5.5" fill="var(--green)"/>
          <path d="M7 6c-1 1-1 3 1 5s4 3 5 2l-1.5-1.5-1 .8c-1-.5-2-1.5-2.5-2.5l.8-1L7 6z" fill="#fff"/>
        </svg>
        <span>5550 1827</span>
      </li>
      <li>
        <svg class="contact-icon" viewBox="0 0 20 20" aria-hidden="true">
          <polygon points="10,1 18,5.5 18,14.5 10,19 2,14.5 2,5.5" fill="var(--green)"/>
          <rect x="5.5" y="7" width="9" height="6" fill="none" stroke="#fff" stroke-width="1.2"/>
          <polyline points="5.5,7 10,10.5 14.5,7" fill="none" stroke="#fff" stroke-width="1.2"/>
        </svg>
        <span>hello@lanternfieldmail.com</span>
      </li>
      <li>
        <svg class="contact-icon" viewBox="0 0 20 20" aria-hidden="true">
          <polygon points="10,1 18,5.5 18,14.5 10,19 2,14.5 2,5.5" fill="var(--green)"/>
          <circle cx="10" cy="10" r="4.5" fill="none" stroke="#fff" stroke-width="1.2"/>
          <line x1="5.5" y1="10" x2="14.5" y2="10" stroke="#fff" stroke-width="1"/>
          <ellipse cx="10" cy="10" rx="2" ry="4.5" fill="none" stroke="#fff" stroke-width="1"/>
        </svg>
        <span>lanternfield-advisory.com</span>
      </li>
    </ul>
  </section>

  <section class="card card-front" aria-label="Business card, logo side">
    <div class="front-logo">
      <span class="brand-square"></span>
      <span class="brand-name">Lanternfield Advisory</span>
    </div>
  </section>

</body>
</html>
```